Pathways to Brightmoor Land Ventures

size of the ad - 8”x 10.75" plus 0.25" bleed
I would like an ad for a magazine that will stand out and make people want to read the ad.
The ad should not be crowded and people reading the ad will be able to read the text.
I would like it to be a creative and modern-day design.
the list of topics should not be the focus of the ad.
the text is attached.
If you decide to use people in the ad then please no ladies.
please note that leave over 1 inch for the bottom of the footer

```html
<!DOCTYPE html>
<html lang="en">
<head>
<meta charset="utf-8">
<title>Real Estate Course – Pathways to Brightmoor Land Ventures</title>
<link rel="stylesheet" href="https://fonts.googleapis.com/css2?family=Raleway:ital,wght@0,400;0,500;0,700;0,800;1,500&display=swap">
<style>
  :root {
    --sky-top: #a6ddf0;
    --sky-mid: #b9cfd9;
    --haze: #9aa6ae;
    --haze-dark: #6f7c84;
    --ground: #c9d2d8;
    --brand-blue: #1a9ad8;
    --title-blue: #1d93d2;
    --navy: #283a8f;
    --tag-blue: #1b74c4;
    --ink: #1b1b1b;
    --white: #ffffff;
    --suit-light: #3a4f9a;
    --suit-dark: #1f2c66;
  }
  * { margin: 0; padding: 0; box-sizing: border-box; }
  html, body { width: 941px; height: 1200px; overflow: hidden; background: #000; }
  .ad {
    position: relative;
    width: 941px;
    height: 1200px;
    overflow: hidden;
    font-family: "Raleway", sans-serif;
    background:
      linear-gradient(180deg, var(--sky-top) 0%, var(--sky-top) 15%, var(--sky-mid) 30%, var(--haze) 50%, var(--haze-dark) 66%, var(--ground) 78%, #e2e7ea 90%);
  }
  .portrait {
    position: absolute;
    left: 420px;
    top: 250px;
    width: 521px;
    height: 838px;
    border-radius: 220px 220px 0 0;
    background: radial-gradient(ellipse at 60% 35%, var(--suit-light) 0%, var(--suit-dark) 75%);
  }
  .headline { position: absolute; left: 0; top: 0; }
  .headline .title { font-weight: 800; fill: var(--title-blue); }
  .headline .subtitle { font-weight: 500; fill: var(--navy); }
  .tagline {
    position: absolute;
    left: 58px;
    top: 210px;
    font-style: italic;
    font-weight: 500;
    font-size: 29px;
    line-height: 37px;
    color: var(--tag-blue);
  }
  .bubble {
    position: absolute;
    border-radius: 50%;
    background: var(--brand-blue);
    color: var(--white);
    display: flex;
    align-items: center;
    justify-content: center;
    text-align: center;
  }
  .bubble-audience {
    left: 59px; top: 336px; width: 190px; height: 190px;
    font-size: 20px; line-height: 27px; font-weight: 400;
  }
  .bubble-offer {
    left: 299px; top: 431px; width: 168px; height: 168px;
    font-size: 25px; line-height: 30px; font-weight: 400;
  }
  .details {
    position: absolute;
    left: 56px;
    top: 625px;
    color: var(--white);
    font-size: 22px;
    line-height: 31px;
    font-weight: 400;
    list-style: none;
  }
  .details .scholarship { margin-top: 6px; font-size: 21px; }
  .topics {
    position: absolute;
    left: 47px;
    top: 843px;
    color: var(--ink);
    font-size: 14.5px;
    line-height: 20px;
  }
  .topics h2 { font-size: 14.5px; font-weight: 700; }
  .topics ul { list-style: none; }
  .footer-band {
    position: absolute;
    left: 0; bottom: 0;
    width: 941px; height: 112px;
    background: var(--brand-blue);
  }
</style>
</head>
<body>
<main class="ad">
  <div class="portrait" role="img" aria-label="Photograph of a young businessman in a blue suit with arms crossed"></div>

  <svg class="headline" width="941" height="170" viewBox="0 0 941 170">
    <text class="title" x="36" y="99" font-size="86" textLength="870" lengthAdjust="spacingAndGlyphs">REAL ESTATE COURSE</text>
    <text class="subtitle" x="38" y="156" font-size="38" textLength="865" lengthAdjust="spacingAndGlyphs">PATHWAYS TO BRIGHTMOOR LAND VENTURES</text>
  </svg>

  <p class="tagline">INVESTING IN KNOWLEDGE IS<br>INVESTING IN OPPORTUNITIES</p>

  <div class="bubble bubble-audience">For those that<br>started or would<br>like to go into<br>real estate</div>
  <div class="bubble bubble-offer">Early Bird<br>Special</div>

  <ul class="details">
    <li>Alder Springs</li>
    <li>10 - Tuesday evenings sessions</li>
    <li>Starting Feb. 28</li>
    <li class="scholarship">Limited Partial Scholarships</li>
  </ul>

  <section class="topics">
    <h2>Topics: Partial Listing</h2>
    <ul>
      <li>- Real estate investment strategies</li>
      <li>- Due diligence</li>
      <li>- Financing</li>
      <li>- Underwriting</li>
      <li>- Property management</li>
      <li>- Real estate Legal basics</li>
      <li>- Sourcing deals</li>
      <li>- Syndication</li>
      <li>- Dealing with brokers</li>
      <li>- Tax fundamentals</li>
    </ul>
  </section>

  <div class="footer-band"></div>
</main>
</body>
</html>
```